New Website Design for Rides for Heroes.org - A Site for People to Donate Cars to War / Disabled Ve

Current site: www.ridesforheroes.org; Look at these sites for ideas: bikez2tots.org; gearsforhopes.org; www.autosformarines.org; www.trucksforsoldiers.org

Industry/Entity Type

Charity

Coding

Coded - Design and coding required

Number of Pages Required

1 page

Requirements
Must have
• n/a
Nice to have
• n/a
Should not have
• n/a

```html
<!DOCTYPE html>
<html lang="en">
<head>
<meta charset="utf-8">
<title>Rides for Heroes – Donate Your Car</title>
<link href="https://fonts.googleapis.com/css2?family=Roboto:wght@400;500;700&family=Ubuntu:wght@300;400;500;700&display=swap" rel="stylesheet">
<style>
:root{
  --brand-blue:#1a7bc4;
  --header-red:#6b0019;
  --green:#7dc243;
  --footer-green:#8cc63f;
  --footer-blue:#2f62ae;
  --button-navy:#1b4f86;
  --gray-band:#eeeeee;
  --text:#333333;
  --muted:#555555;
  --field-border:#cfcfcf;
  --white:#ffffff;
}
*{margin:0;padding:0;box-sizing:border-box}
html,body{width:1200px;height:2250px;overflow:hidden;background:var(--white)}
body{position:relative;font-family:'Roboto',sans-serif;color:var(--text)}
.abs{position:absolute}

/* Header */
.site-header{left:0;top:0;width:1200px;height:90px;background:var(--header-red)}
.header-brand-band{left:0;top:0;width:375px;height:90px}
.brand{left:92px;top:28px;display:flex;align-items:center;gap:10px}
.brand-mark{width:32px;height:32px;border-radius:50%;background:#c8161d}
.brand-name{font-family:'Roboto',sans-serif;font-weight:500;font-size:20px;color:var(--white)}
.main-nav{left:440px;top:38px;display:flex;gap:34px}
.main-nav a{font-size:13px;color:var(--white);text-decoration:none;font-weight:500;text-transform:uppercase}
.help-line{right:165px;top:14px;text-align:right;color:var(--white);line-height:1}
.help-line .ask{font-size:18px;font-weight:400}
.help-line .call{font-size:21px;font-weight:700;margin-top:4px}
.help-line .live{font-size:11.5px;margin-top:4px;font-weight:500}
.chat-icon{left:1043px;top:17px}

/* Hero */
.hero{left:0;top:90px;width:1200px;height:505px;background:linear-gradient(180deg,#2f8fdc 0%,#6cb7ec 45%,#a8d8f5 68%,#86c25a 80%,#5fa93a 100%)}
.hero-vehicle{left:0;top:245px;width:565px;height:260px;background:linear-gradient(180deg,#3a9a4a 0%,#2f7d3b 35%,#e9e9e6 60%,#bfbfbf 100%);border-top-right-radius:60px}
.hero-title{left:92px;top:178px;font-family:'Ubuntu',sans-serif;font-size:48px;line-height:54px;color:var(--white);font-weight:400;letter-spacing:-1.5px}
.hero-title strong{font-weight:500;display:block}
.donate-form{left:644px;top:143px;width:460px;height:407px;background:var(--white);border:2px solid #dfe6ee;box-shadow:0 2px 8px rgba(0,0,0,.15)}
.form-kicker{position:absolute;top:18px;width:100%;text-align:center;font-family:'Ubuntu',sans-serif;font-size:25px;color:var(--brand-blue)}
.form-title{position:absolute;top:44px;width:100%;text-align:center;font-family:'Ubuntu',sans-serif;font-size:35px;font-weight:700;color:var(--brand-blue)}
.form-note{position:absolute;top:84px;width:100%;text-align:center;font-size:16px;color:var(--text)}
.field{position:absolute;width:207px;height:38px;border:1px solid var(--field-border);font-size:12.5px;color:#888;padding:12px 0 0 8px}
.donate-button{position:absolute;left:17px;top:334px;width:424px;height:44px;background:var(--green);color:var(--white);font-size:17px;font-weight:700;text-align:center;line-height:44px;text-transform:uppercase}

/* Section headings */
.section-title{width:1200px;text-align:center;font-family:'Ubuntu',sans-serif;font-size:38px;font-weight:400;color:var(--brand-blue)}

/* How it works */
.step{width:220px;text-align:center}
.step-icon{width:96px;height:96px;border:2px solid var(--green);border-radius:50%;margin:0 auto;display:flex;align-items:center;justify-content:center}
.step-label{margin-top:18px;font-size:18px;font-weight:700;color:var(--text);text-transform:uppercase}

/* Why */
.why-band{left:0;top:993px;width:1200px;height:597px;background:var(--gray-band)}
.tow-truck{left:95px;top:1180px;width:405px;height:270px;background:linear-gradient(180deg,#eeeeee 0%,#e9a23a 35%,#2d82c7 60%,#333 90%,#eeeeee 100%);border-radius:10px}
.reasons{left:528px;top:1158px;width:570px;list-style:none}
.reasons li{position:relative;padding-left:42px;font-size:13.5px;line-height:21px;color:var(--muted);height:76px}
.reasons li strong{color:var(--text);font-weight:500}
.reasons svg{position:absolute;left:0;top:6px}

/* Safe */
.badge-business{left:248px;top:1742px;width:150px;height:52px;background:#1b7d9e;border-radius:4px}
.badge-grade{left:402px;top:1743px;width:50px;height:50px;background:#1b7d9e;border-radius:50%}
.badge-charity{left:538px;top:1728px;width:100px;height:80px;background:#2a8ac8;border-radius:50%}
.badge-secure{left:745px;top:1738px;width:160px;height:58px;background:#c8161d;border-radius:4px}

/* Footer */
.site-footer{left:0;top:1886px;width:1200px;height:364px;background:var(--footer-blue)}
.footer-heading{font-family:'Ubuntu',sans-serif;font-size:17px;font-weight:400;color:var(--footer-green)}
.footer-about{left:92px;top:2000px;width:320px;font-size:14px;line-height:25px;color:var(--white)}
.footer-links{list-style:none;font-size:14px;line-height:25px;color:var(--white)}
.subscribe-input{left:873px;top:2013px;width:235px;height:40px;background:var(--white);color:#777;font-size:13px;padding:12px 0 0 9px}
.send-button{left:873px;top:2063px;width:94px;height:40px;background:var(--button-navy);color:var(--white);font-size:12px;font-weight:500;display:flex;align-items:center;justify-content:center;gap:6px}
.follow{left:873px;top:2127px;display:flex;align-items:center;gap:10px;font-family:'Ubuntu',sans-serif;font-size:17px;color:var(--footer-green)}
.follow span.dot{width:12px;height:12px;border-radius:50%;background:var(--white)}
.copyright{left:0;top:2214px;width:1200px;text-align:center;font-size:13px;color:var(--white)}
</style>
</head>
<body>

<header class="abs site-header">
  <svg class="abs header-brand-band" width="375" height="90" viewBox="0 0 375 90">
    <polygon points="0,0 350,0 375,45 350,90 0,90" fill="#1f5fb0"/>
    <polygon points="0,0 345,0 368,45 345,84 0,84" fill="#2f86d9"/>
  </svg>
  <div class="abs brand"><span class="brand-mark"></span><span class="brand-name">Rides for Heroes</span></div>
  <nav class="abs main-nav">
    <a href="#">Home</a><a href="#">How it works</a><a href="#">Why us</a><a href="#">Contact</a>
  </nav>
  <div class="abs help-line">
    <div class="ask">we need your help</div>
    <div class="call">Call 1-800-555-0142</div>
    <div class="live">Live operators Available(24X7)</div>
  </div>
  <svg class="abs chat-icon" width="68" height="56" viewBox="0 0 68 56" fill="none" stroke="#3a9be6" stroke-width="3">
    <path d="M6 22a20 16 0 1 1 12 14l-10 6 3-9A16 16 0 0 1 6 22z"/>
    <path d="M40 20a20 16 0 1 1 6 30l8 5-1-9"/>
    <circle cx="18" cy="22" r="1.5" fill="#3a9be6"/><circle cx="26" cy="22" r="1.5" fill="#3a9be6"/>
    <circle cx="44" cy="36" r="1.5" fill="#3a9be6"/><circle cx="52" cy="36" r="1.5" fill="#3a9be6"/>
  </svg>
</header>

<section class="abs hero">
  <div class="abs hero-vehicle" role="img" aria-label="Photo of a classic green and white pickup truck parked on a grassy field"></div>
</section>
<h1 class="abs hero-title">Donate your car to a wet,<strong>make a difference</strong></h1>

<form class="abs donate-form">
  <div class="form-kicker">DONATE</div>
  <div class="form-title">YOUR CAR HERE!</div>
  <div class="form-note">Please fill out form or Call toll-free 1-800-555-0142</div>
  <div class="field" style="left:17px;top:126px">Name</div>
  <div class="field" style="left:234px;top:126px">Email</div>
  <div class="field" style="left:17px;top:178px">Phone Number</div>
  <div class="field" style="left:234px;top:178px">Cell Phone</div>
  <div class="field" style="left:17px;top:230px">Address</div>
  <div class="field" style="left:234px;top:230px">City</div>
  <div class="field" style="left:17px;top:280px">State</div>
  <div class="field" style="left:234px;top:280px">Zip Code</div>
  <div class="donate-button">Donate now</div>
</form>

<h2 class="abs section-title" style="top:664px">How it works</h2>
<div class="abs step" style="left:142px;top:764px">
  <div class="step-icon">
    <svg width="52" height="52" viewBox="0 0 52 52" fill="none" stroke="#222" stroke-width="2.5" stroke-linejoin="round">
      <path d="M12 6l8 10-5 5c3 7 9 13 16 16l5-5 10 8-5 7C25 47 5 27 5 11z"/>
    </svg>
  </div>
  <div class="step-label">Call us</div>
</div>
<div class="abs step" style="left:487px;top:764px">
  <div class="step-icon">
    <svg width="60" height="44" viewBox="0 0 60 44" fill="none" stroke="#222" stroke-width="2.5" stroke-linejoin="round">
      <path d="M4 30h52v6H4z"/><path d="M30 30V14h14l8 10v6"/><path d="M8 30L22 8"/>
      <circle cx="14" cy="38" r="4"/><circle cx="44" cy="38" r="4"/>
    </svg>
  </div>
  <div class="step-label">We tow it</div>
</div>
<div class="abs step" style="left:835px;top:764px">
  <div class="step-icon">
    <svg width="50" height="50" viewBox="0 0 50 50" fill="none" stroke="#222" stroke-width="2.5" stroke-linejoin="round">
      <path d="M34 6l10 10-24 24-13 3 3-13z"/><path d="M29 11l10 10"/><path d="M10 30l10 10"/>
    </svg>
  </div>
  <div class="step-label">Tax write-off</div>
</div>
<svg class="abs" style="left:372px;top:802px" width="106" height="20" viewBox="0 0 106 20" fill="none" stroke="#aaa" stroke-width="2">
  <path d="M2 10q13-10 26 0t26 0 26 0 24 0"/>
</svg>
<svg class="abs" style="left:720px;top:802px" width="106" height="20" viewBox="0 0 106 20" fill="none" stroke="#aaa" stroke-width="2">
  <path d="M2 10q13-10 26 0t26 0 26 0 24 0"/>
</svg>

<section class="abs why-band"></section>
<h2 class="abs section-title" style="top:1060px">Why donate your car to us?</h2>
<div class="abs tow-truck" role="img" aria-label="Illustration of a blue flatbed tow truck carrying an orange car"></div>
<ul class="abs reasons">
  <li><svg width="20" height="16" viewBox="0 0 20 16"><path d="M2 9l5 5L18 2" fill="none" stroke="#6db33f" stroke-width="2.5"/></svg><strong>CRB A+ Rated &amp; IRS 501(c)3 Approved:</strong> Free 24/7 Pickup with No<br>DMV Hassles.</li>
  <li><svg width="20" height="16" viewBox="0 0 20 16"><path d="M2 9l5 5L18 2" fill="none" stroke="#6db33f" stroke-width="2.5"/></svg><strong>Free Local Towing:</strong> We will pick up your car donation, running or not, when it's most<br>convenient, at home or work.</li>
  <li><svg width="20" height="16" viewBox="0 0 20 16"><path d="M2 9l5 5L18 2" fill="none" stroke="#6db33f" stroke-width="2.5"/></svg><strong>All Cars Accepted:</strong> We take your car regardless of its condition or<br>registration status.</li>
  <li><svg width="20" height="16" viewBox="0 0 20 16"><path d="M2 9l5 5L18 2" fill="none" stroke="#6db33f" stroke-width="2.5"/></svg><strong>Income Tax Deduction:</strong> We issue you an IRS tax receipt &amp; offer the largest resale<br>network to get you the highest tax write-off possible.</li>
  <li><svg width="20" height="16" viewBox="0 0 20 16"><path d="M2 9l5 5L18 2" fill="none" stroke="#6db33f" stroke-width="2.5"/></svg><strong>No Paperwork Hassles:</strong> We take any car and handle everything: DMV, Smog and<br>IRS paperwork.</li>
</ul>

<h2 class="abs section-title" style="top:1644px">Safe &amp; Secure</h2>
<div class="abs badge-business" role="img" aria-label="Accredited business badge"></div>
<div class="abs badge-grade" role="img" aria-label="Rating badge"></div>
<div class="abs badge-charity" role="img" aria-label="Approved charity seal"></div>
<div class="abs badge-secure" role="img" aria-label="Secure site badge"></div>

<footer class="abs site-footer"></footer>
<h3 class="abs footer-heading" style="left:92px;top:1961px">About us</h3>
<p class="abs footer-about">There are many variations of passages of Lorem Ipsum available, on the majority have suffered alteration in some form, by a injected humour, or randomised words which do look even slightly believable. If you are going to use a passage of the Lorem Ipsum generators.</p>
<h3 class="abs footer-heading" style="left:492px;top:1961px">Useful links</h3>
<ul class="abs footer-links" style="left:492px;top:2000px"><li>Home</li><li>Donate now</li><li>How it works</li><li>Why us?</li></ul>
<h3 class="abs footer-heading" style="left:667px;top:1961px">Support</h3>
<ul class="abs footer-links" style="left:667px;top:2000px"><li>Contact us</li><li>Call us</li><li>Privacy</li><li>terms &amp; services</li></ul>
<h3 class="abs footer-heading" style="left:873px;top:1961px">Subscribe our Newleter for free</h3>
<div class="abs subscribe-input">Enter your email address</div>
<div class="abs send-button">
  <svg width="14" height="12" viewBox="0 0 14 12"><path d="M0 5L14 0 11 12 7 8 12 2 5 7z" fill="#fff"/></svg>SEND
</div>
<div class="abs follow">Follow us: <span class="dot"></span><span class="dot"></span><span class="dot"></span><span class="dot"></span></div>
<div class="abs copyright">©2016 Rides for Heroes. All rights reserved</div>

</body>
</html>
```